Menu Design Project

Hi there!

We're looking to create a kick ass menu for our new restaurant. Our restaurant will be open all day from 10Am till midnight, the kitchen does not close. We will be selling burgers, burritos, pizzas, saladas, cocktails, international beers, sandwiches, wraps.

Our restaurant it's located in Sevilla, Spain. 99% of the restaurants in Sevilla sell tapas & tradional food from Spain but we are sick of that, so we've created this restaurant!

www.Plaznook.com/CorvenaBar

We're targeting all type of people: young travelers, young locals, parents & kids, first time date, you know, everyone!

We will have:

breakfast - Brunch
Lunch & dinner
Happy hour drinks & cocktails
Sandwiches, wraps & pizzas

```html
<!DOCTYPE html>
<html lang="eo">
<head>
<meta charset="utf-8">
<title>Corvena Bar — Menuo</title>
<link rel="stylesheet" href="https://fonts.googleapis.com/css2?family=Arimo:wght@400;700&family=Open+Sans:wght@700&family=Pacifico&display=swap">
<style>
  :root {
    --stage: #e8e3dc;
    --frame-orange: #f4a93a;
    --ink: #111111;
    --stamp-red: #f0384a;
    --stamp-blue: #3aaee8;
    --brush-blue: #3aaee8;
    --brush-orange: #f4a93a;
    --brush-red: #c8321e;
  }
  * { margin: 0; padding: 0; box-sizing: border-box; }
  html, body { width: 963px; height: 1200px; overflow: hidden; }
  body { background: var(--stage); position: relative; font-family: "Arimo", Arial, sans-serif; color: var(--ink); }

  .menu {
    position: absolute; left: 66px; top: 62px; width: 820px; height: 1091px;
    background: var(--frame-orange);
    box-shadow: 3px 3px 0 #ffffff;
  }
  .panel { position: absolute; top: 21px; width: 367px; height: 1047px; overflow: hidden; }
  .panel--left { left: 21px; }
  .panel--right { left: 430px; }
  .panel__backdrop {
    position: absolute; inset: 0;
    background: linear-gradient(180deg, #eeeeee 0%, #e6e6e6 45%, #dcdcdc 75%, #e4e4e4 100%);
  }

  .photo { position: absolute; }
  .photo--sandwich {
    left: 21px; top: 21px; width: 218px; height: 290px;
    background: linear-gradient(160deg, #b9a58a 0%, #8c6a48 40%, #d9d3c9 75%, #f2f2f2 100%);
  }
  .photo--dessert {
    left: 243px; top: 68px; width: 202px; height: 145px;
    background: radial-gradient(circle at 55% 40%, #c56a28 0%, #a8612f 22%, #d9d2c6 42%, #6f7d8c 75%, #4d5966 100%);
  }

  .stamp {
    position: absolute; left: 56px; top: 295px; width: 306px; height: 138px;
    border: 4px dashed var(--stamp-blue);
    background: #ffffff;
    transform: rotate(-4deg);
    display: flex; align-items: center; justify-content: center; text-align: center;
    font-family: "Open Sans", Arial, sans-serif; font-weight: 700;
    color: var(--stamp-red); font-size: 23px; line-height: 25px;
  }

  .section-title {
    position: absolute; font-family: "Pacifico", cursive; font-size: 46px; line-height: 1; color: var(--ink);
    white-space: nowrap;
  }
  .section-title--sandwiches { left: 101px; top: 452px; font-size: 48px; }
  .section-title--salads { left: 463px; top: 64px; font-size: 45px; }
  .section-title--pizzas { left: 555px; top: 473px; font-size: 45px; }
  .brush { position: absolute; }

  .sandwiches { position: absolute; left: 65px; top: 531px; width: 300px; list-style: none; font-size: 11.5px; line-height: 14.9px; }
  .sandwiches li { margin-bottom: 13.8px; }
  .sandwiches .dish-name { display: block; }

  .salads { position: absolute; left: 430px; top: 148px; width: 367px; list-style: none; text-align: center; font-size: 13.6px; line-height: 23.4px; }
  .salads li { margin-bottom: 23.4px; }

  .pizzas { position: absolute; left: 478px; top: 559px; width: 320px; list-style: none; font-size: 16px; line-height: 29.6px; white-space: nowrap; }
</style>
</head>
<body>
<main class="menu">
  <div class="panel panel--left"><div class="panel__backdrop" role="img" aria-label="Faded black and white view of Sevilla streets"></div></div>
  <div class="panel panel--right"><div class="panel__backdrop" role="img" aria-label="Faded black and white view of the Sevilla cathedral and palm trees"></div></div>

  <div class="photo photo--sandwich" role="img" aria-label="Photo of stacked pressed sandwiches with greens on a plate"></div>
  <div class="photo photo--dessert" role="img" aria-label="Photo of a bowl of caramelised dessert with lime wedges"></div>

  <div class="stamp">Matenmanĝo- Brunch<br>Lunĉo &amp; vespermanĝo<br>Feliĉaj horoj trinkaĵoj<br>&amp; koktelo</div>

  <h2 class="section-title section-title--sandwiches">Sandviĉoj,</h2>
  <svg class="brush" style="left:96px; top:511px;" width="220" height="12" viewBox="0 0 220 12"><path d="M3 9 C60 5 140 3 217 2 L212 7 C140 7 70 9 8 11 Z" fill="var(--brush-blue)"/></svg>

  <ul class="sandwiches">
    <li><span class="dish-name">BridgePork</span>Prosciutto cotto, Manchego cheese, red pepper mayo, red onions and field greens. $9.57</li>
    <li><span class="dish-name">Bocadillo De La Mancha</span>Jamon Serrano, Manchego cheese, membrillo, whole grain dijon mustard and field greens. $9.57</li>
    <li><span class="dish-name">Blue Pig n' Fig</span>Jamon Serrano, Velmarra Reserve blue cheese, local fig and black tea preserve, whole grain dijon mustard and field greens. $9.57</li>
    <li><span class="dish-name">Grant Park Grinder</span>Hand-made Salame Milano, Mortadella &amp; Coppa, fresh mozzarella, piparras, tomatoes, red wine vinaigrette and field greens. $10.02</li>
    <li><span class="dish-name">Panino Di Prosciutto</span>San Danielle Prosciutto, Varello cheese, olive oil, cracked black pepper and field greens. $9.57</li>
    <li><span class="dish-name">BLTA</span>House-made prosciutto bacon, mayonnaise, fresh tomatoes, avocado and field greens. $6.15</li>
    <li><span class="dish-name">Salumi Piccante</span>Calabrese salami, Varello cheese, locally-made spicy giardiniera, mayo and field greens. $9.11</li>
    <li><span class="dish-name">Sandwich Campagne</span>Country pate, Gruyere cheese, whole grain dijon mustard and cornichons. $7.97</li>
  </ul>

  <h2 class="section-title section-title--salads">Supervestajxoj</h2>
  <svg class="brush" style="left:498px; top:117px;" width="165" height="14" viewBox="0 0 165 14"><path d="M3 11 C50 6 110 4 162 3 L158 8 C110 9 60 11 8 13 Z" fill="var(--brush-orange)"/></svg>

  <ul class="salads">
    <li>Caprese Pastorale<br>Fresh mozzarella, basil-fennel pesto, tomatoes<br>and cracked black pepper. (V) $7.52</li>
    <li>Cali Chevre<br>Goat cheese, house-made almond butter,<br>avocado, shaved celery and red onions. (V) $7.52</li>
    <li>Farmhouse Veggie Deluxe<br>Manchego cheese, avocado, green apple,<br>cucumber, balsamic vinaigrette, whole grain dijon<br>mustard and field greens. $7.52</li>
  </ul>

  <h2 class="section-title section-title--pizzas">Picoj</h2>
  <svg class="brush" style="left:498px; top:516px;" width="220" height="16" viewBox="0 0 220 16"><path d="M3 13 C60 8 140 5 217 4 L213 9 C140 10 70 12 8 15 Z" fill="var(--brush-red)"/></svg>

  <ul class="pizzas">
    <li>Margherita</li>
    <li>Fresh tomato, mozzarella &amp; oregano, on a</li>
    <li>Tomato Base</li>
    <li>Hawaiian</li>
    <li>Ham &amp; Pineapple, on a Tomato Base</li>
    <li>Capricciosa</li>
    <li>Ham, Mushrooms &amp; Kalamata Olives, on a</li>
    <li>Tomato Base</li>
    <li>Aussie</li>
    <li>Ham, Bacon &amp; Egg, on a Tomato Base</li>
    <li>Napoletana</li>
    <li>Mozzarella, Kalamata olives, Anchovies &amp;</li>
    <li>Basil, on a Tomato Base</li>
    <li>Peperoni</li>
    <li>Peperoni &amp; Mozzarella on a Tomato Base</li>
  </ul>
</main>
</body>
</html>
```